Party Sticker Designs for Kids Parties

I need 13 Sticker Designs for 13 different kid parties. Also, several stickers with have multiple versions: same design, but different texts. All versions will need to have both a 3x3 round and 3x3 square design. I’ve provided a lot of examples and stock designs. My design notes (summer2020_DesignGraphic_Notes) include the look I like best on the left and some other ideas on the right – the main goal is a good design. We will need all stickers in jpg, eps, png, psd, and ai formats.

```html
<!DOCTYPE html>
<html lang="en">
<head>
<meta charset="utf-8">
<title>Bee Party Stickers – Square and Round</title>
<link rel="stylesheet" href="https://fonts.googleapis.com/css2?family=Baloo+2:wght@700&display=swap">
<style>
  :root {
    --honey-yellow: #ffe01a;
    --stripe-grey: #5d5e60;
    --label-white: #ffffff;
    --ink-black: #1c1c1c;
    --page-white: #ffffff;
    --bee-yellow: #f7d21c;
    --bee-dark: #2a2a2a;
  }
  html, body {
    margin: 0;
    padding: 0;
    width: 1200px;
    height: 365px;
    overflow: hidden;
    background: var(--page-white);
  }
  .sticker-sheet {
    position: relative;
    width: 1200px;
    height: 365px;
  }
  .sticker {
    position: absolute;
    top: 51px;
    width: 242px;
    height: 242px;
  }
  .sticker--what-square { left: 38px; }
  .sticker--what-round  { left: 323px; }
  .sticker--bday-square { left: 617px; }
  .sticker--bday-round  { left: 904px; }

  .honey-field { fill: var(--honey-yellow); }
  .grey-stripe { fill: var(--stripe-grey); }
  .centre-label { fill: var(--label-white); }
  .dashed-ring {
    fill: none;
    stroke: var(--stripe-grey);
    stroke-width: 1.6;
    stroke-dasharray: 3 3;
  }
  .label-text {
    font-family: "Baloo 2", "Fredoka", sans-serif;
    font-weight: 700;
    font-size: 17px;
    fill: var(--ink-black);
    text-anchor: middle;
  }
</style>
</head>
<body>
<main class="sticker-sheet">

  <!-- Square sticker: What will it BEE ? -->
  <svg class="sticker sticker--what-square" viewBox="0 0 242 242" aria-label="Square sticker: What will it BEE ?">
    <defs>
      <linearGradient id="bee-tones-1" x1="0" y1="0" x2="1" y2="1">
        <stop offset="0" stop-color="var(--bee-yellow)"/>
        <stop offset="1" stop-color="var(--bee-dark)"/>
      </linearGradient>
    </defs>
    <rect class="honey-field" x="0" y="0" width="242" height="242" role="img" aria-label="Yellow honeycomb pattern background"/>
    <rect class="grey-stripe" x="0" y="80" width="242" height="10"/>
    <rect class="grey-stripe" x="0" y="102" width="242" height="10"/>
    <rect class="grey-stripe" x="0" y="130" width="242" height="10"/>
    <rect class="grey-stripe" x="0" y="152" width="242" height="10"/>
    <circle class="centre-label" cx="121" cy="121" r="73"/>
    <circle class="dashed-ring" cx="121" cy="121" r="66"/>
    <ellipse cx="121" cy="122" rx="32" ry="26" fill="url(#bee-tones-1)" role="img" aria-label="Cartoon bumblebee illustration"/>
    <text class="label-text" x="121" y="91">What will</text>
    <text class="label-text" x="121" y="164">it BEE ?</text>
  </svg>

  <!-- Round sticker: What will it BEE ? -->
  <svg class="sticker sticker--what-round" viewBox="0 0 242 242" aria-label="Round sticker: What will it BEE ?">
    <defs>
      <clipPath id="round-cut-1"><circle cx="121" cy="121" r="121"/></clipPath>
      <linearGradient id="bee-tones-2" x1="0" y1="0" x2="1" y2="1">
        <stop offset="0" stop-color="var(--bee-yellow)"/>
        <stop offset="1" stop-color="var(--bee-dark)"/>
      </linearGradient>
    </defs>
    <g clip-path="url(#round-cut-1)">
      <circle class="honey-field" cx="121" cy="121" r="121" role="img" aria-label="Yellow honeycomb pattern background"/>
      <rect class="grey-stripe" x="0" y="80" width="242" height="10"/>
      <rect class="grey-stripe" x="0" y="102" width="242" height="10"/>
      <rect class="grey-stripe" x="0" y="130" width="242" height="10"/>
      <rect class="grey-stripe" x="0" y="152" width="242" height="10"/>
    </g>
    <circle class="centre-label" cx="121" cy="121" r="73"/>
    <circle class="dashed-ring" cx="121" cy="121" r="66"/>
    <ellipse cx="121" cy="122" rx="32" ry="26" fill="url(#bee-tones-2)" role="img" aria-label="Cartoon bumblebee illustration"/>
    <text class="label-text" x="121" y="91">What will</text>
    <text class="label-text" x="121" y="164">it BEE ?</text>
  </svg>

  <!-- Square sticker: Happy BEE-day -->
  <svg class="sticker sticker--bday-square" viewBox="0 0 242 242" aria-label="Square sticker: Happy BEE-day">
    <defs>
      <linearGradient id="bee-tones-3" x1="0" y1="0" x2="1" y2="1">
        <stop offset="0" stop-color="var(--bee-yellow)"/>
        <stop offset="1" stop-color="var(--bee-dark)"/>
      </linearGradient>
    </defs>
    <rect class="honey-field" x="0" y="0" width="242" height="242" role="img" aria-label="Yellow honeycomb pattern background"/>
    <rect class="grey-stripe" x="0" y="80" width="242" height="10"/>
    <rect class="grey-stripe" x="0" y="102" width="242" height="10"/>
    <rect class="grey-stripe" x="0" y="130" width="242" height="10"/>
    <rect class="grey-stripe" x="0" y="152" width="242" height="10"/>
    <circle class="centre-label" cx="121" cy="121" r="73"/>
    <circle class="dashed-ring" cx="121" cy="121" r="66"/>
    <ellipse cx="121" cy="122" rx="32" ry="26" fill="url(#bee-tones-3)" role="img" aria-label="Cartoon bumblebee illustration"/>
    <text class="label-text" x="121" y="91">Happy</text>
    <text class="label-text" x="121" y="164">BEE-day</text>
  </svg>

  <!-- Round sticker: Happy BEE-day -->
  <svg class="sticker sticker--bday-round" viewBox="0 0 242 242" aria-label="Round sticker: Happy BEE-day">
    <defs>
      <clipPath id="round-cut-2"><circle cx="121" cy="121" r="121"/></clipPath>
      <linearGradient id="bee-tones-4" x1="0" y1="0" x2="1" y2="1">
        <stop offset="0" stop-color="var(--bee-yellow)"/>
        <stop offset="1" stop-color="var(--bee-dark)"/>
      </linearGradient>
    </defs>
    <g clip-path="url(#round-cut-2)">
      <circle class="honey-field" cx="121" cy="121" r="121" role="img" aria-label="Yellow honeycomb pattern background"/>
      <rect class="grey-stripe" x="0" y="80" width="242" height="10"/>
      <rect class="grey-stripe" x="0" y="102" width="242" height="10"/>
      <rect class="grey-stripe" x="0" y="130" width="242" height="10"/>
      <rect class="grey-stripe" x="0" y="152" width="242" height="10"/>
    </g>
    <circle class="centre-label" cx="121" cy="121" r="73"/>
    <circle class="dashed-ring" cx="121" cy="121" r="66"/>
    <ellipse cx="121" cy="122" rx="32" ry="26" fill="url(#bee-tones-4)" role="img" aria-label="Cartoon bumblebee illustration"/>
    <text class="label-text" x="121" y="91">Happy</text>
    <text class="label-text" x="121" y="164">BEE-day</text>
  </svg>

</main>
</body>
</html>
```